Loyalty/Discount Card Design Project

Loyalty card design for pennynest.co.uk. Disregard current site graphics!! Open to all colors/concepts. Back and front. Will require all .ai files please. No need to round corners.

Illustrator (ai) card template included with bleed for your convenience.

Target Market(s)

Shoppers looking to save money locally

Requirements
Must have
• Front:
(i)Card name (PennyNest)
(ii)Tagline (for discounts and special offers in Haverhill)
(iii)URL (www.pennynest.co.uk)

Back:
(i)Space for barcode and QR code.
(ii)Dummy small print like a credit card
(iii)Signature strip.

Spec:

4/4 (cmyk)
300 dpi
ai files/eps files/

Nice to have
• Would like the design to say 'save money' even if the text wasn't present.

```html
<!DOCTYPE html>
<html lang="en">
<head>
<meta charset="utf-8">
<title>PennyNest Loyalty Card</title>
<link href="https://fonts.googleapis.com/css2?family=Archivo+Black&family=Arimo:wght@400;700&display=swap" rel="stylesheet">
<style>
  :root {
    --page: #ffffff;
    --card-blue: #1a3fd8;
    --card-blue-deep: #1530b8;
    --card-blue-light: #5a7ae0;
    --card-green: #3a9a3c;
    --card-yellow: #f2e600;
    --trim-cyan: #7fd8e8;
    --guide-red: #d0443a;
    --brand-yellow: #e8f000;
    --tag-yellow: #ffe100;
    --url-navy: #1c2a9a;
    --code-green: #1f7a2a;
    --ink: #000000;
    --white: #ffffff;
    --fine-print: #dfe6ff;
    --pattern: rgba(150, 170, 235, 0.35);
  }
  html, body {
    margin: 0;
    padding: 0;
    width: 926px;
    height: 1200px;
    overflow: hidden;
    background: var(--page);
  }
  .canvas {
    position: relative;
    width: 926px;
    height: 1200px;
  }
  .card {
    position: absolute;
    left: 21px;
    width: 889px;
    height: 569px;
    box-sizing: border-box;
    border: 3px solid var(--trim-cyan);
    overflow: hidden;
    font-family: "Arimo", Arial, sans-serif;
  }
  .card::after {
    content: "";
    position: absolute;
    inset: 14px;
    border: 1.5px dashed var(--guide-red);
    pointer-events: none;
  }
  .card--front {
    top: 8px;
    background: linear-gradient(to bottom, var(--card-blue) 0%, var(--card-blue) 72%, var(--card-green) 90%, var(--card-yellow) 100%);
  }
  .card--back {
    top: 614px;
    background: var(--card-blue);
  }
  .currency-pattern {
    position: absolute;
    background: radial-gradient(ellipse at center, var(--pattern) 0%, rgba(150,170,235,0) 70%);
  }
  .front-pattern { left: 60px; top: 280px; width: 640px; height: 220px; }
  .card-name {
    position: absolute;
    right: 60px;
    top: 50px;
    margin: 0;
    font-family: "Archivo Black", "Arial Black", sans-serif;
    font-weight: 400;
    font-size: 104px;
    line-height: 1;
    letter-spacing: -1px;
    color: var(--brand-yellow);
  }
  .tagline {
    position: absolute;
    right: 60px;
    top: 180px;
    margin: 0;
    text-align: right;
    font-size: 37px;
    line-height: 60px;
    color: var(--tag-yellow);
  }
  .purse-art {
    position: absolute;
    left: 650px;
    top: 320px;
    width: 175px;
    height: 165px;
    border-radius: 50%;
    background: radial-gradient(circle at 45% 55%, #c8281e 0%, #a81a14 55%, #ffffff 56%, #ffffff 100%);
  }
  .site-url {
    position: absolute;
    margin: 0;
    font-size: 31px;
  }
  .card--front .site-url { left: 38px; top: 495px; color: var(--url-navy); }
  .card--back .site-url { left: 38px; top: 58px; color: var(--tag-yellow); font-size: 28px; }
  .back-pattern-top { left: 40px; top: 110px; width: 800px; height: 160px; }
  .back-pattern-bottom { left: 40px; top: 420px; width: 640px; height: 120px; }
  .code-space {
    position: absolute;
    background: var(--code-green);
    display: flex;
    align-items: center;
    justify-content: center;
    text-align: center;
    color: var(--ink);
  }
  .barcode-space {
    left: 518px;
    top: 55px;
    width: 345px;
    height: 74px;
    font-size: 31px;
  }
  .qr-space {
    left: 753px;
    top: 140px;
    width: 110px;
    height: 110px;
    font-size: 20px;
    line-height: 1.2;
  }
  .waves {
    position: absolute;
    left: 0;
    top: 0;
    width: 883px;
    height: 563px;
  }
  .signature-label {
    position: absolute;
    left: 150px;
    top: 367px;
    margin: 0;
    font-size: 31px;
    color: var(--ink);
  }
  .small-print {
    position: absolute;
    left: 38px;
    top: 478px;
    width: 470px;
    margin: 0;
    font-size: 13px;
    line-height: 1.35;
    color: var(--fine-print);
  }
  .back-name {
    position: absolute;
    right: 45px;
    top: 490px;
    margin: 0;
    font-family: "Archivo Black", "Arial Black", sans-serif;
    font-size: 50px;
    line-height: 1;
    color: var(--white);
  }
</style>
</head>
<body>
<main class="canvas">
  <section class="card card--front">
    <div class="currency-pattern front-pattern" role="img" aria-label="Faint pattern of pound and dollar symbols"></div>
    <h1 class="card-name">PennyNest</h1>
    <p class="tagline">For Discounts and Special Offers<br>in Haverhill</p>
    <div class="purse-art" role="img" aria-label="Illustration of a red purse stuffed with banknotes and coins"></div>
    <p class="site-url">www.pennynest.co.uk</p>
  </section>

  <section class="card card--back">
    <div class="currency-pattern back-pattern-top" role="img" aria-label="Faint pattern of pound and dollar symbols"></div>
    <div class="currency-pattern back-pattern-bottom" role="img" aria-label="Faint pattern of pound and dollar symbols"></div>
    <svg class="waves" viewBox="0 0 883 563" aria-hidden="true">
      <path d="M0 300 L300 255 L520 290 L620 270 L883 260 L883 285 L620 300 L520 320 L300 285 L0 330 Z" fill="var(--card-green)"/>
      <path d="M0 330 L300 285 L520 320 L620 300 L883 285 L883 370 L620 385 L520 410 L300 370 L0 420 Z" fill="var(--card-yellow)"/>
      <path d="M0 420 L300 370 L520 410 L620 385 L883 370 L883 395 L620 410 L520 432 L300 395 L0 445 Z" fill="var(--card-blue-deep)"/>
      <path d="M0 445 L300 395 L520 432 L620 410 L883 395 L883 410 L620 428 L520 448 L300 412 L0 460 Z" fill="var(--card-blue-light)"/>
    </svg>
    <p class="site-url">www.pennynest.co.uk</p>
    <div class="code-space barcode-space">for barcode</div>
    <div class="code-space qr-space">for<br>QR code</div>
    <p class="signature-label">Signature strip</p>
    <p class="small-print">This card remains the property of PennyNest. Present it at participating Haverhill shops. Not transferable. Offers may change without notice.</p>
    <p class="back-name">PennyNest</p>
  </section>
</main>
</body>
</html>
```